R.T. Halvorsen Electric Holiday Party Invitation

We need a cohesive, on-brand holiday party invitation suite for R.T. Halvorsen Electrical Contractors (slogan Powered Past Limits). Design should include: 1) 5x7" invitation (print + digital), 2) matching RSVP card, and 3) raffle ticket.
Use our brand colors (navy, red, white, light gray) and modern professional style with subtle holiday accents.
Event: Thursday, Dec 18 2025 | 6-10 PM | Brambleton Hall, 418 Larkspur Ave, Hammonton NJ 08094.
RSVP by: Dec 1 | Plus one allowed.
Deliver print-ready PDFs + editable source files.

```html
<!DOCTYPE html>
<html lang="en">
<head>
<meta charset="utf-8">
<title>R.T. Halvorsen Electric – Holiday Party Invitation</title>
<link rel="stylesheet" href="https://fonts.googleapis.com/css2?family=Tinos:ital,wght@0,700;1,700&family=Lobster&display=swap">
<style>
  :root {
    --gray: #cacbd8;
    --navy: #153553;
    --red: #fb0006;
    --white: #ffffff;
    --ink: #111111;
    --haze: #e3e4ec;
  }
  * { box-sizing: border-box; margin: 0; padding: 0; }
  html, body { width: 1200px; height: 800px; overflow: hidden; background: var(--white); }
  .invitation {
    position: relative;
    width: 1200px;
    height: 800px;
    overflow: hidden;
    background: var(--gray);
    font-family: "Tinos", "Times New Roman", serif;
  }
  .backdrop { position: absolute; inset: 0; width: 100%; height: 100%; }

  .slogan {
    position: absolute;
    left: 0; right: 0; top: 52px;
    text-align: center;
    font-weight: 700;
    font-size: 98px;
    line-height: 1;
    color: var(--white);
    text-shadow: 4px 4px 0 var(--navy);
    letter-spacing: -1px;
  }

  .celebration-art {
    position: absolute;
    left: 73px; top: 150px;
    width: 470px; height: 262px;
    border-radius: 40% 40% 30% 30%;
    background: radial-gradient(ellipse at center, var(--haze) 0%, rgba(227,228,236,0.6) 55%, rgba(202,203,216,0) 75%);
  }

  .raffle-title {
    position: absolute;
    left: 308px; top: 302px;
    transform: translate(-50%, -50%) rotate(-11deg);
    white-space: nowrap;
    font-weight: 700;
    font-size: 78px;
    line-height: 1;
    color: var(--navy);
  }

  .party-line {
    position: absolute;
    transform: translate(-50%, -50%) rotate(-22deg);
    white-space: nowrap;
    font-style: italic;
    font-weight: 700;
    font-size: 66px;
    line-height: 1;
    color: var(--white);
    letter-spacing: 2px;
  }
  .party-line--holiday { left: 846px; top: 282px; }
  .party-line--party { left: 814px; top: 352px; }
  .party-script {
    position: absolute;
    left: 846px; top: 428px;
    transform: translate(-50%, -50%) rotate(-19deg);
    white-space: nowrap;
    font-family: "Lobster", cursive;
    font-size: 124px;
    line-height: 1;
    color: var(--white);
  }

  .event-ticket {
    position: absolute;
    left: 34px; top: 388px;
    width: 282px; height: 378px;
    background: var(--red);
    padding: 9px;
  }
  .event-ticket__inner {
    width: 100%; height: 100%;
    background: var(--white);
    border: 5px dotted var(--red);
    outline: 1px dashed var(--navy);
    outline-offset: -9px;
    display: flex;
    flex-direction: column;
    align-items: center;
    padding: 36px 22px 0;
  }
  .rule { width: 100%; border-top: 2px dashed var(--navy); }
  .rule--red { border-top-color: var(--red); }
  .event-ticket__label {
    font-weight: 700;
    font-size: 42px;
    line-height: 1;
    color: var(--red);
    margin: 6px 0 8px;
  }
  .event-ticket__when {
    font-weight: 700;
    font-size: 30px;
    line-height: 1.25;
    color: var(--ink);
    text-align: center;
    margin: 8px 0 8px;
  }
  .event-ticket__where {
    font-weight: 700;
    font-size: 15px;
    line-height: 1.4;
    color: var(--ink);
    text-align: center;
    margin-top: 28px;
  }
  .spacer { height: 18px; }

  .rsvp-stub {
    position: absolute;
    left: 328px; top: 694px;
    width: 373px; height: 71px;
    background: var(--navy);
    border: 3px solid var(--gray);
    color: var(--gray);
    font-weight: 700;
    font-size: 29px;
    line-height: 1.08;
    text-align: center;
    padding-top: 2px;
  }
  .rsvp-stub::before, .rsvp-stub::after {
    content: "";
    position: absolute;
    top: 50%;
    width: 22px; height: 22px;
    margin-top: -11px;
    border-radius: 50%;
    background: var(--white);
  }
  .rsvp-stub::before { left: -11px; }
  .rsvp-stub::after { right: -11px; }

  .brand {
    position: absolute;
    left: 705px; top: 660px;
    width: 462px;
    text-align: center;
    color: var(--red);
    font-weight: 700;
  }
  .brand__mark {
    display: block;
    width: 34px; height: 34px;
    margin: 0 auto 10px;
    border-radius: 50%;
    background: var(--red);
  }
  .brand__name { font-size: 44px; line-height: 1; letter-spacing: 2px; }
  .brand__trade { font-size: 22px; line-height: 1.3; letter-spacing: 5px; }
</style>
</head>
<body>
<main class="invitation">
  <svg class="backdrop" viewBox="0 0 1482 1058" preserveAspectRatio="none" aria-hidden="true">
    <path class="swoosh-navy-top" fill="var(--navy)" d="M1120,0 L1305,0 L1010,330 L960,330 Q1060,170 1120,0 Z"/>
    <path class="swoosh-navy-low" fill="var(--navy)" d="M1482,500 L1482,660 C1200,650 1000,790 620,860 C420,895 200,905 0,895 L0,830 C250,870 450,850 640,800 C950,720 1150,560 1482,500 Z"/>
    <path class="swoosh-red" fill="var(--red)" d="M1305,0 L1482,0 L1482,222 C1250,420 1000,640 620,850 C450,885 250,900 0,870 L0,793 C250,890 520,820 740,590 C920,400 1100,200 1305,0 Z"/>
    <path class="footer-white" fill="var(--white)" d="M0,895 C300,905 700,850 1000,770 C1200,690 1350,640 1482,650 L1482,1058 L0,1058 Z"/>
    <polygon class="burst" fill="var(--red)" points="1310,470 1194,519 1270,620 1144,604 1160,730 1059,654 1010,770 961,654 860,730 876,604 750,620 826,519 710,470 826,421 750,320 876,336 860,210 961,286 1010,170 1059,286 1160,210 1144,336 1270,320 1194,421"/>
    <line class="raffle-rule" x1="42" y1="405" x2="720" y2="262" stroke="var(--red)" stroke-width="3" stroke-dasharray="10 7"/>
    <line class="raffle-rule" x1="42" y1="505" x2="720" y2="360" stroke="var(--red)" stroke-width="3" stroke-dasharray="10 7"/>
  </svg>

  <h1 class="slogan">Powered Past Limits</h1>

  <div class="celebration-art" role="img" aria-label="Faint illustration of a celebrating crowd with stars, theatre masks and party streamers"></div>

  <p class="raffle-title">Raffle Ticket</p>

  <p class="party-line party-line--holiday">HOLIDAY</p>
  <p class="party-line party-line--party">PARTY</p>
  <p class="party-script">Invitation</p>

  <section class="event-ticket">
    <div class="event-ticket__inner">
      <div class="rule"></div>
      <p class="event-ticket__label">Event:</p>
      <div class="rule"></div>
      <div class="spacer"></div>
      <div class="rule rule--red"></div>
      <p class="event-ticket__when">Thursday<br>Dec 18 2025<br>6-10 PM</p>
      <div class="rule rule--red"></div>
      <p class="event-ticket__where">Brambleton Hall,<br>418 Larkspur Ave,<br>Hammonton NJ 08094.</p>
    </div>
  </section>

  <p class="rsvp-stub">RSVP by: Dec 1<br>Plus one allowed.</p>

  <div class="brand">
    <span class="brand__mark" aria-hidden="true"></span>
    <p class="brand__name">R.T. HALVORSEN</p>
    <p class="brand__trade">Electrical Contractor</p>
  </div>
</main>
</body>
</html>
```